Meridian Signal sales for the nema region

Business card that is informative and unique. Whether the card can be applicable to a real world application or it is 3D or if something changed on the card. I want it to be an eye catcher

Went on vacation/holiday

```html
<!DOCTYPE html>
<html lang="en">
<head>
<meta charset="utf-8">
<title>Meridian Signal – Business Card</title>
<link rel="stylesheet" href="https://fonts.googleapis.com/css2?family=Open+Sans:wght@400;600;700&display=swap">
<style>
  :root {
    --brand-magenta: #c0134a;
    --brand-magenta-soft: #cb3262;
    --brand-grey: #6d6b6c;
    --ink: #2b2b2b;
    --rule: #d4d4d4;
    --card-white: #ffffff;
    --backdrop: #e9e9eb;
  }
  * { margin: 0; padding: 0; box-sizing: border-box; }
  html, body {
    width: 1200px;
    height: 782px;
    overflow: hidden;
    background: var(--backdrop);
    font-family: "Open Sans", Arial, sans-serif;
  }
  .canvas {
    position: relative;
    width: 1200px;
    height: 782px;
  }
  .card {
    position: absolute;
    top: 242px;
    width: 520px;
    height: 298px;
    box-shadow: 0 6px 18px rgba(0,0,0,0.15);
  }
  /* Front side */
  .card-front {
    left: 50px;
    background: var(--card-white);
    border-bottom: 9px solid var(--brand-magenta);
  }
  .brand-lockup {
    position: absolute;
    left: 28px;
    top: 92px;
    width: 210px;
    display: flex;
    flex-direction: column;
    align-items: center;
    gap: 14px;
  }
  .brand-square {
    width: 46px;
    height: 46px;
    background: var(--brand-magenta);
  }
  .brand-name {
    font-weight: 700;
    font-size: 22px;
    letter-spacing: 1.5px;
    color: var(--brand-magenta);
    text-transform: uppercase;
    white-space: nowrap;
  }
  .divider {
    position: absolute;
    left: 262px;
    top: 70px;
    width: 1px;
    height: 150px;
    background: var(--rule);
  }
  .contact {
    position: absolute;
    left: 286px;
    top: 84px;
    color: var(--ink);
    text-transform: uppercase;
  }
  .contact-name {
    font-weight: 700;
    font-size: 16px;
    letter-spacing: 0.8px;
    color: var(--brand-magenta);
    line-height: 1.2;
  }
  .contact-title {
    font-size: 11px;
    letter-spacing: 0.6px;
    margin-bottom: 6px;
  }
  .contact-line {
    display: flex;
    align-items: center;
    gap: 6px;
    font-size: 11.5px;
    letter-spacing: 0.5px;
    line-height: 1.55;
  }
  .contact-line svg { width: 10px; height: 10px; flex: none; fill: var(--brand-magenta); }
  .contact-address {
    font-size: 11.5px;
    letter-spacing: 0.5px;
    line-height: 1.45;
    margin-top: 2px;
  }
  /* Back side */
  .card-back {
    left: 630px;
    background: var(--brand-magenta);
    overflow: hidden;
  }
  .monogram-field {
    position: absolute;
    inset: 0;
    background: linear-gradient(135deg, var(--brand-magenta-soft) 0%, var(--brand-magenta) 100%);
  }
  .back-brand {
    position: absolute;
    right: 30px;
    bottom: 96px;
    font-weight: 700;
    font-size: 15px;
    letter-spacing: 1.2px;
    color: var(--card-white);
    text-transform: uppercase;
  }
</style>
</head>
<body>
<main class="canvas">
  <section class="card card-front" aria-label="Business card front">
    <div class="brand-lockup">
      <span class="brand-square"></span>
      <span class="brand-name">Meridian Signal</span>
    </div>
    <div class="divider"></div>
    <div class="contact">
      <p class="contact-name">Elias Varen</p>
      <p class="contact-title">Managing Director</p>
      <p class="contact-line">
        <svg viewBox="0 0 10 10" aria-hidden="true"><path d="M2 0.5 L3.6 0.5 L4.3 2.8 L3.2 3.6 Q4.2 5.8 6.4 6.8 L7.2 5.7 L9.5 6.4 L9.5 8 Q9.5 9.5 8 9.5 Q0.5 9 0.5 2 Q0.5 0.5 2 0.5 Z"/></svg>
        055-310 742 918
      </p>
      <p class="contact-line">
        <svg viewBox="0 0 10 10" aria-hidden="true"><path d="M0.5 2 H9.5 V8.5 H0.5 Z M0.5 2 L5 5.6 L9.5 2" /></svg>
        hello@meridian.example
      </p>
      <p class="contact-line">
        <svg viewBox="0 0 10 10" aria-hidden="true"><circle cx="5" cy="5" r="4.5"/><path d="M1 4.5 H9 M5 0.6 V9.4" stroke="#fff" stroke-width="0.7" fill="none"/></svg>
        www.meridiansignal.example
      </p>
      <p class="contact-address">87, Harbour Road Lane.<br>30918, Coastline</p>
    </div>
  </section>

  <section class="card card-back" aria-label="Business card back">
    <div class="monogram-field" role="img" aria-label="Repeating brand monogram pattern in soft magenta tones"></div>
    <span class="back-brand">Meridian Signal</span>
  </section>
</main>
</body>
</html>
```